Business Card Design Project

We are a distribution company providing goods to Latin America. We sell everything from Medical equipment, generic medicines, to carecliners. The logo that we use is attached. The logo can incorporate different colors other than black for versatility. The company name is Valdoria International Corporation and/or VIC. The card will be printed using 1 or more of the following: Silk mounted and/or embossed. So if the design ideas could be made to incorporate that technique or any other unique techniques, it would be great. The target market is dialysis centers/doctors.

Basic Info for card:
Marnie Dowsett
Purchasing Manager
555-317-4086 direct
555-241-7953 fax
marnie.dowsett@valdoriavic.example
www.valdoriavic.example

Target Market(s)

Latin America

Industry/Entity Type

Business

Requirements
Nice to have
• The Front of the card should have the basic contact information with company name/logo. The back of the card could incorporate

```html
<!DOCTYPE html>
<html lang="en">
<head>
<meta charset="utf-8">
<title>Valdoria International Corporation – Business Card</title>
<link rel="stylesheet" href="https://fonts.googleapis.com/css2?family=Saira+Condensed:wght@400;500&display=swap">
<style>
  :root {
    --green-top: #0f4f1f;
    --green-bottom: #020d05;
    --ink-green: #14401a;
    --paper: #ffffff;
    --footer: #07170b;
    --light: #ffffff;
  }
  html, body {
    margin: 0;
    padding: 0;
    width: 1200px;
    height: 733px;
    overflow: hidden;
    background: var(--paper);
  }
  .card {
    position: relative;
    width: 1200px;
    height: 733px;
    font-family: "Saira Condensed", "Arial Narrow", sans-serif;
    color: var(--ink-green);
    overflow: hidden;
  }
  .brand-band {
    position: absolute;
    left: 0; top: 0;
    width: 1200px; height: 372px;
    background: linear-gradient(180deg, var(--green-top) 0%, var(--green-bottom) 100%);
  }
  .company-name {
    position: absolute;
    right: 612px;
    top: 72px;
    margin: 0;
    text-align: right;
    color: var(--light);
    font-weight: 400;
    text-transform: uppercase;
    line-height: 1;
  }
  .company-name span { display: block; }
  .company-name .line-1 { font-size: 122px; line-height: 112px; letter-spacing: 2px; }
  .company-name .line-2 { font-size: 78px; line-height: 70px; letter-spacing: 1px; }
  .company-name .line-3 { font-size: 94px; line-height: 84px; letter-spacing: 1px; }

  .contact-lines {
    position: absolute;
    left: 66px;
    top: 430px;
    margin: 0;
    padding: 0;
    list-style: none;
  }
  .contact-lines li {
    font-size: 50px;
    line-height: 70px;
    white-space: nowrap;
  }
  .contact-lines .label {
    font-size: 32px;
    margin-left: 22px;
  }
  .contact-lines .web { font-size: 46px; }

  .person {
    position: absolute;
    right: 60px;
    top: 418px;
    text-align: right;
  }
  .person-name {
    margin: 0;
    font-weight: 400;
    font-size: 72px;
    line-height: 80px;
    letter-spacing: 1px;
  }
  .person-title {
    margin: 0;
    font-size: 54px;
    line-height: 66px;
  }
  .person-email {
    margin: 8px 0 0;
    font-size: 42px;
    line-height: 60px;
  }

  .address-band {
    position: absolute;
    left: 0; top: 660px;
    width: 1200px; height: 73px;
    background: var(--footer);
    color: var(--light);
    text-align: center;
    font-size: 36px;
    line-height: 73px;
  }
</style>
</head>
<body>
  <div class="card">
    <header class="brand-band">
      <h1 class="company-name">
        <span class="line-1">Valdoria</span>
        <span class="line-2">International</span>
        <span class="line-3">Corporation</span>
      </h1>
    </header>

    <ul class="contact-lines">
      <li>555-317-4086<span class="label">direct</span></li>
      <li>555-241-7953<span class="label">fax</span></li>
      <li class="web">www.valdoriavic.example</li>
    </ul>

    <div class="person">
      <h2 class="person-name">Marnie Dowsett</h2>
      <p class="person-title">Purchasing Manager</p>
      <p class="person-email">marnie.dowsett@valdoriavic.example</p>
    </div>

    <footer class="address-band">4817 SW 12th Avenue Port Alden, FL 30000</footer>
  </div>
</body>
</html>
```